make a fireworks website

we are manufacturer of fireworks in Asia.
we need a HD fireworks website for showing product to all world customers.
we also need an register for member system,location, forum,products..etc
I added my Logo for the company.
brightnova.com.hk

and please message me if you have
any question.
here some example of website:
http://www.skyplumeshow.com/
http://www.tornelupyro.com/
http://www.quarvel-pyro.co.uk/
http://www.mirethpyro.co.uk/

```html
<!DOCTYPE html>
<html lang="en">
<head>
<meta charset="utf-8">
<title>Brightnova – Fireworks</title>
<link rel="stylesheet" href="https://fonts.googleapis.com/css2?family=Arimo:wght@400;700&family=Russo+One&family=Anton&display=swap">
<style>
:root{
  --topbar:#3b3b3b;
  --navbar:#2a2a2a;
  --pink:#ee1b5d;
  --yellow:#ffe400;
  --card-dark:#454545;
  --card-light:#f4f4f4;
  --text-grey:#7a7a7a;
  --footer:#2b2f38;
  --footer-panel:#24272d;
  --footer-text:#a7abb2;
  --white:#ffffff;
}
*{margin:0;padding:0;box-sizing:border-box}
html,body{width:1200px;height:1128px;overflow:hidden;background:var(--white)}
body{position:relative;font-family:"Arimo",Arial,sans-serif;color:var(--text-grey)}
.abs{position:absolute}

.top-bar{left:0;top:0;width:1200px;height:23px;background:var(--topbar)}
.cart-badge{left:758px;top:0;width:24px;height:23px;background:var(--pink)}
.cart-badge svg{position:absolute;left:5px;top:5px}
.account-links{left:786px;top:6px;font-size:8px;color:var(--white);white-space:nowrap}
.nav-bar{left:0;top:23px;width:1200px;height:45px;background:var(--navbar)}
.nav-item{top:23px;height:45px;line-height:45px;font-size:7.5px;color:var(--white);text-align:center}
.nav-item.active{background:var(--pink)}
.brand-box{left:307px;top:0;width:149px;height:79px;background:#eeeeee;display:flex;align-items:center;justify-content:center;gap:7px}
.brand-dot{width:22px;height:22px;border-radius:50%;background:var(--pink)}
.brand-name{font-size:19px;font-weight:700;color:#3a3a3a}

.hero{left:0;top:68px;width:1200px;height:403px;
  background:radial-gradient(ellipse at 50% 25%,#c9406a 0%,rgba(160,40,110,.6) 25%,transparent 55%),
  linear-gradient(180deg,#2a0a33 0%,#4d1450 45%,#8a1f4a 78%,#2a1020 100%)}
.hero-title{left:675px;top:189px;font-family:"Russo One",Arial,sans-serif;font-size:14px;line-height:17px;color:var(--white);letter-spacing:.3px}
.hero-copy{left:675px;top:237px;font-size:9.5px;line-height:11.5px;color:var(--white)}
.hero-copy em{font-style:normal;color:var(--yellow)}
.btn-yellow{left:675px;top:272px;width:98px;height:29px;background:var(--yellow);color:#111;font-family:"Anton",Impact,sans-serif;font-size:13px;line-height:29px;text-align:center}

.card{top:435px;width:188px;height:202px}
.card-head{left:0;top:0;width:188px;height:36px;background:var(--card-dark);border-bottom:3px solid var(--pink);color:var(--white);font-size:14.5px;line-height:36px;padding-left:12px}
.card-photo{left:7px;top:45px;width:174px;height:77px;border-radius:0 0 50% 50%/0 0 18px 18px;
  background:radial-gradient(circle at 50% 55%,#d9e6ff 0%,#5a78c8 20%,#1c1c3a 55%,#3a1a20 100%)}
.card-copy{left:14px;top:131px;width:160px;font-size:8.5px;line-height:10px;color:var(--text-grey)}
.card-foot{left:0;top:165px;width:188px;height:38px}
.card-link{left:0;top:191px;width:188px;text-align:center;font-size:7.5px;font-weight:700;color:#9a9a9a}
.card-shadow{left:34px;top:210px;width:120px;height:8px;border-radius:50%;background:radial-gradient(ellipse,#e2e2e2,transparent 70%)}
.card-form{background:var(--card-dark)}
.form-intro{left:14px;top:49px;width:165px;font-size:8.5px;line-height:10.5px;color:var(--white)}
.form-field{left:16px;width:157px;height:24px;background:var(--white);border:2px solid #cfcfcf;font-size:8.5px;line-height:20px;padding-left:10px;color:#9a9a9a}

.displays{left:0;top:708px;width:1200px;height:224px;background:#000}
.displays-photo{left:440px;top:708px;width:470px;height:224px;
  background:radial-gradient(ellipse at 42% 30%,#f4e6d6 0%,#b19b8a 18%,#4a3b33 45%,#0c0c0c 80%)}
.displays-title{left:307px;top:765px;font-size:19px;font-weight:700;color:var(--pink)}
.displays-copy{left:307px;top:804px;width:375px;font-size:10px;line-height:11px;color:var(--pink)}
.btn-pink{left:307px;top:862px;width:83px;height:25px;background:var(--pink);color:#111;font-family:"Anton",Impact,sans-serif;font-size:10.5px;line-height:25px;text-align:center}

.footer{left:0;top:932px;width:1200px;height:196px;background:var(--footer)}
.footer-panel{left:704px;top:932px;width:188px;height:196px;background:var(--footer-panel)}
.footer-head{top:964px;font-size:11px;color:var(--footer-text)}
.footer-list{top:992px;list-style:none;font-size:8.5px;line-height:10.6px;color:var(--footer-text)}
.footer-rule{left:307px;top:1084px;width:349px;height:1px;background:#4a4f58}
.copyright{left:307px;top:1099px;font-size:7.5px;color:var(--footer-text)}
.footer-brand{left:704px;top:980px;width:188px;display:flex;align-items:center;justify-content:center;gap:7px}
.footer-brand .brand-dot{background:#9a9ea5;width:20px;height:20px}
.footer-brand .brand-name{color:#b3b6bb;font-size:17px}
.footer-panel-rule{left:744px;top:1030px;width:111px;height:1px;background:#3d4148}
.social-row{left:759px;top:1047px;display:flex;gap:3px}
.social-dot{width:18px;height:18px;border-radius:50%;background:#9a9ea5}
.social-dot.blue{background:#3b78c2}
</style>
</head>
<body>

<header>
  <div class="abs top-bar"></div>
  <div class="abs nav-bar"></div>
  <div class="abs cart-badge"><svg width="14" height="13" viewBox="0 0 14 13"><path d="M0 1h3l2 7h7l2-5H4" fill="none" stroke="#fff" stroke-width="1.5"/><circle cx="6" cy="11" r="1.3" fill="#fff"/><circle cx="11" cy="11" r="1.3" fill="#fff"/></svg></div>
  <div class="abs account-links">Your Cart &nbsp;|&nbsp; Wish List &nbsp;|&nbsp; Checkout</div>
  <div class="abs brand-box"><span class="brand-dot"></span><span class="brand-name">brightnova</span></div>
  <nav>
    <div class="abs nav-item active" style="left:575px;width:42px">HOME</div>
    <div class="abs nav-item" style="left:626px;width:50px">ABOUT US</div>
    <div class="abs nav-item" style="left:693px;width:50px">PRODUCTS</div>
    <div class="abs nav-item" style="left:759px;width:50px">LOCATION</div>
    <div class="abs nav-item" style="left:822px;width:60px">CUSTOM LINK</div>
  </nav>
</header>

<section>
  <div class="abs hero" role="img" aria-label="Night sky with bursting fireworks over a lake and lit hillside hotel"></div>
  <h1 class="abs hero-title">We bring the nighttime skies<br>to life for all occasions</h1>
  <p class="abs hero-copy">Get Exclusive <em>Offer</em> and<br>Saving &amp; Join Our <em>Email List</em> for more offers.</p>
  <a class="abs btn-yellow">SHOP NOW</a>
</section>

<section>
  <div class="abs card" style="left:307px">
    <svg class="abs card-foot" viewBox="0 0 188 38" preserveAspectRatio="none"><path d="M0 0 Q94 30 188 0 V26 Q94 50 0 26Z" fill="var(--card-light)"/></svg>
    <h2 class="abs card-head">Best Blast Firework</h2>
    <div class="abs card-photo" role="img" aria-label="Close-up of a blue firework burst"></div>
    <p class="abs card-copy">Our team works year around to make sure you receive the highest quality fireworks in the entire industry.</p>
    <a class="abs card-link">Click Here</a>
    <div class="abs card-shadow"></div>
  </div>

  <div class="abs card" style="left:506px">
    <svg class="abs" style="left:0;top:0" width="188" height="203" viewBox="0 0 188 203"><path d="M0 0H188V165Q94 195 0 165Z" fill="var(--card-dark)"/><path d="M0 165 Q94 195 188 165 V191 Q94 215 0 191Z" fill="var(--card-light)"/></svg>
    <h2 class="abs card-head">Get Products</h2>
    <p class="abs form-intro">User can select a product and find they can get it</p>
    <div class="abs form-field" style="top:77px">Select Category</div>
    <div class="abs form-field" style="top:107px">Select Product</div>
    <div class="abs form-field" style="top:138px">Your Location</div>
    <a class="abs card-link">Submit</a>
    <div class="abs card-shadow"></div>
  </div>

  <div class="abs card" style="left:706px">
    <svg class="abs card-foot" viewBox="0 0 188 38" preserveAspectRatio="none"><path d="M0 0 Q94 30 188 0 V26 Q94 50 0 26Z" fill="var(--card-light)"/></svg>
    <h2 class="abs card-head">Special Offers</h2>
    <div class="abs card-photo" role="img" aria-label="Close-up of a blue firework burst"></div>
    <p class="abs card-copy">Our team works year around to make sure you receive the highest quality fireworks in the entire industry.</p>
    <a class="abs card-link">Click Here</a>
    <div class="abs card-shadow"></div>
  </div>
</section>

<section>
  <div class="abs displays"></div>
  <div class="abs displays-photo" role="img" aria-label="Couple watching a white fountain firework display at night"></div>
  <h2 class="abs displays-title">Professional Firework Displays</h2>
  <p class="abs displays-copy">Our team works year around to make sure you receive the highest quality fireworks in the entire industry. We believe that the quality, visual performance, and varied effects of our fireworks are unsurpassed in the consumer fireworks industry.</p>
  <a class="abs btn-pink">SHOP NOW</a>
</section>

<footer>
  <div class="abs footer"></div>
  <div class="abs footer-panel"></div>
  <h3 class="abs footer-head" style="left:307px">PRODUCTS</h3>
  <ul class="abs footer-list" style="left:307px">
    <li>Featured Products</li><li>New For 2014</li><li>Maximum Charge</li><li>Assortments</li><li>Aerials &amp; Finales</li><li>Reloadables</li>
  </ul>
  <ul class="abs footer-list" style="left:418px">
    <li>Rockets</li><li>Roman Candles</li><li>Rockets</li><li>Firecrackers</li><li>Novelties &amp; Sparklers</li><li>California</li>
  </ul>
  <h3 class="abs footer-head" style="left:545px">SITE OVERVIEW</h3>
  <ul class="abs footer-list" style="left:548px">
    <li>Home</li><li>About Us</li><li>Online Store</li><li>Fireworks Displays</li><li>Our Locations</li>
  </ul>
  <div class="abs footer-rule"></div>
  <p class="abs copyright">Copyright © 2014 Company Name. All Rights Reserved.</p>
  <div class="abs footer-brand"><span class="brand-dot"></span><span class="brand-name">brightnova</span></div>
  <div class="abs footer-panel-rule"></div>
  <div class="abs social-row" aria-label="Social links">
    <span class="social-dot blue"></span><span class="social-dot"></span><span class="social-dot"></span><span class="social-dot"></span>
  </div>
</footer>

</body>
</html>
```